Ecommerce Website

Hello designers of Pixel Harbor,

Today I'm requesting webpage designs for my new start up business in Toronto Canada. I have little or no experience in this field so I decided to outsource it here! My business revolves around the retail of customizable smartphone cases, as well as other objects such as mouse pads, mugs, etc.. Our main focus is smartphone cases, tablets and such. There are a few of these types of websites out already so the idea shouldn't be too foreign. I am looking for a minimalist look for my website revolving around light colours. Should convey a sense of simplistic design with elegant feel while including aspects of the business. Please see current website at brindlecove.ca to see how the set-up is (currently on pre-made template). Should have a similar feel to it. Also i have a post for logo design as i currently do not have one. If you can create a logo as well for my other post along with this one, gives preference to artist.

http://jobs.pixelharbor.com/job.aspx?id=587216
Updates

The design should be transferable to the other webpages on the site. The overall look should be the same (borders, buttons, etc)

I am not sure if I'm allowed to request the page in coding as it said non-coded earlier. However it would be preferable to have the website in CSS or HTML as well as a PSD version for alterations.

Wasn't too clear about the total requirements. We are looking for a main homepage as well as a general design for the rest of our pages such as browsing catalogue page, product page, etc.. Should be a general look that can be used for multiple pages.

I have committed the payment so please do not hesitate to post designs.

To All designers.  I have attached the logo to the brief. It has multiple colors which you can choose from. The last one on the second row is the one i prefer the best however if your site can match well with any other ones, that is okay as well. 

Reason: have a few designs for selection in mind however need to get it to the final point.

Target Market(s)

Young adults ages 19 - 32

Industry/Entity Type

Retail

Requirements
Must have
• Main slider design - Main page will have a slider which displays new products or services. Please see brindlecove.ca for example

Note worthy - Currently we are using a service from http://www.vantoriq.com/ so please make sure that it the design will work with that in mind.

```html
<!DOCTYPE html>
<html lang="en">
<head>
<meta charset="utf-8">
<title>Brindle Cove – Smartphone Cases</title>
<link href="https://fonts.googleapis.com/css2?family=Open+Sans:wght@400;600;700&display=swap" rel="stylesheet">
<style>
:root{
  --green:#7cc520;
  --green-dark:#5e9c12;
  --header:#2b2b2b;
  --header-light:#3a3a3a;
  --ink:#333;
  --muted:#888;
  --line:#dedede;
  --page:#ffffff;
  --backdrop:#e6e6e6;
  --footer:#ececec;
  --footer-bar:#dcdcdc;
  --btn:#222;
}
*{box-sizing:border-box;margin:0;padding:0}
html,body{width:766px;height:1200px;overflow:hidden}
body{background:var(--backdrop);font-family:'Open Sans',Arial,sans-serif;color:var(--ink);position:relative}
.page{position:absolute;left:24px;top:0;width:718px;height:1200px;background:var(--page)}
.abs{position:absolute}

/* header */
.site-header{left:0;top:0;width:718px;height:116px;background:linear-gradient(var(--header-light),var(--header))}
.brand{left:34px;top:16px;display:flex;align-items:center;gap:8px}
.brand-mark{width:26px;height:26px;background:var(--green);border-radius:4px}
.brand-name{font-size:22px;font-weight:700;color:#fff}
.brand-tag{left:68px;top:46px;font-size:8px;color:#aaa;letter-spacing:.5px}
.top-links{right:30px;top:8px;display:flex;gap:16px;font-size:9px;color:#ddd;align-items:center}
.top-links span{display:flex;align-items:center;gap:4px}
.top-links i{display:inline-block;width:9px;height:9px;background:var(--green);border-radius:2px}
.phone{font-weight:700;color:#fff;font-size:10px}
.search{right:30px;top:44px;width:150px;height:20px;background:#555;border-radius:3px}
.search svg{position:absolute;right:6px;top:5px}
.main-nav{left:30px;top:84px;display:flex;gap:4px}
.main-nav a{display:block;padding:0 14px;height:28px;line-height:28px;background:var(--green);color:#fff;font-size:11px;font-weight:600;text-decoration:none;border-radius:3px 3px 0 0}
.nav-rule{left:0;top:112px;width:718px;height:4px;background:var(--green)}

/* slider */
.slider{left:30px;top:132px;width:658px;height:200px;border:1px solid var(--line);background:#fff}
.slide-title{left:20px;top:24px;font-size:26px;font-weight:700;color:#222}
.slide-sub{left:20px;top:62px;font-size:11px;font-weight:700;color:var(--green)}
.slide-copy{left:20px;top:80px;width:190px;font-size:7.5px;line-height:11px;color:var(--muted)}
.slide-price{left:20px;top:116px;font-size:18px;font-weight:700;color:#222}
.slide-old{left:90px;top:123px;font-size:9px;color:var(--muted);text-decoration:line-through}
.shop-btn{left:20px;top:146px;width:80px;height:22px;line-height:22px;text-align:center;background:var(--btn);color:#fff;font-size:9px;font-weight:700;border-radius:2px}
.dots{left:20px;top:184px;display:flex;gap:5px}
.dots b{width:6px;height:6px;border-radius:50%;background:#ccc}
.dots b:first-child{background:#555}
.slide-case{top:14px;width:96px;height:170px;border-radius:14px}

/* sidebar */
.side-box{left:30px;top:383px;width:162px;height:414px;border:1px solid var(--line);overflow:hidden}
.side-head{height:26px;line-height:26px;padding-left:12px;font-size:11px;font-weight:600;background:#f3f3f3;border-bottom:1px solid var(--line)}
.side-list{list-style:none;padding:5px 14px}
.side-list li{font-size:8px;line-height:17px;color:#555;border-bottom:1px dotted #e4e4e4;padding-left:10px;position:relative}
.side-list li:last-child{border-bottom:0}
.side-list li::before{content:"";position:absolute;left:0;top:7px;width:3px;height:3px;background:var(--green)}

.subscribe{left:30px;top:812px;width:162px;height:135px;border:1px solid var(--line);padding:10px 12px}
.subscribe h3{font-size:14px;color:var(--green);font-weight:600;line-height:16px}
.subscribe h4{font-size:11px;color:#444;font-weight:600}
.subscribe p{font-size:7px;color:var(--muted);margin-top:6px;line-height:10px}
.subscribe .field{margin-top:8px;height:18px;border:1px solid var(--line);font-size:7px;color:#aaa;line-height:16px;padding-left:5px}
.subscribe .go{margin:8px 0 0 auto;width:56px;height:18px;line-height:18px;text-align:center;background:var(--green);color:#fff;font-size:8px;font-weight:600}

/* products */
.grid{left:210px;top:383px;width:478px;display:grid;grid-template-columns:repeat(3,146px);column-gap:20px;row-gap:14px}
.card{height:184px;border:1px solid var(--line);padding:8px;position:relative}
.card .shot{height:118px;border-radius:6px;margin:0 24px}
.card .name{position:absolute;left:8px;top:146px;font-size:8px;color:var(--green);font-weight:600}
.card .price{position:absolute;left:8px;top:160px;font-size:10px;font-weight:700;color:#222}
.card .cart{position:absolute;right:8px;top:158px;width:46px;height:16px;line-height:16px;text-align:center;background:var(--btn);color:#fff;font-size:6.5px;font-weight:600}

/* footer */
.site-footer{left:0;top:980px;width:718px;height:186px;background:var(--footer);border-top:1px solid var(--line)}
.f-col{top:12px}
.f-col h5{font-size:10px;font-weight:600;color:#333;margin-bottom:6px}
.f-col li{list-style:none;font-size:7.5px;line-height:12px;color:#666}
.social{display:flex;gap:4px}
.social b{width:14px;height:14px;background:#7a9cc8;border-radius:2px}
.footer-bar{left:0;top:1166px;width:718px;height:34px;background:var(--footer-bar);font-size:7.5px;color:#666}
.footer-bar .copy{left:30px;top:12px}
.footer-bar .legal{right:30px;top:12px}
</style>
</head>
<body>
<div class="page">

  <header class="site-header abs">
    <div class="brand abs"><span class="brand-mark"></span><span class="brand-name">Brindle Cove</span></div>
    <div class="brand-tag abs">custom cases for every phone</div>
    <div class="top-links abs">
      <span class="phone"><i></i>+1 416 555 0198</span>
      <span><i></i>My Cart</span>
      <span><i></i>Log In</span>
      <span><i></i>My Account</span>
      <span><i></i>Sign Up</span>
    </div>
    <div class="search abs">
      <svg width="10" height="10" viewBox="0 0 10 10"><circle cx="4" cy="4" r="3" fill="none" stroke="#ccc" stroke-width="1.4"/><line x1="6.2" y1="6.2" x2="9" y2="9" stroke="#ccc" stroke-width="1.4"/></svg>
    </div>
    <nav class="main-nav abs">
      <a href="#">Main</a><a href="#">About Us</a><a href="#">Designs</a><a href="#">Create</a><a href="#">Contact</a><a href="#">Request a Quote</a>
    </nav>
    <div class="nav-rule abs"></div>
  </header>

  <section class="slider abs">
    <div class="slide-title abs">Smart Phone</div>
    <div class="slide-sub abs">SMART PHONE &amp; TABLE CASES</div>
    <p class="slide-copy abs">Design your own case online with our easy editor and choose from hundreds of ready made prints.</p>
    <div class="slide-price abs">$20.00</div>
    <div class="slide-old abs">$24.00</div>
    <div class="shop-btn abs">SHOP NOW</div>
    <div class="dots abs"><b></b><b></b><b></b><b></b></div>
    <div class="slide-case abs" style="left:300px;background:linear-gradient(#f4f4f4,#d8d8d8)" role="img" aria-label="White phone case with black pattern print"></div>
    <div class="slide-case abs" style="left:410px;background:linear-gradient(#7c5a3a,#3c4a2a)" role="img" aria-label="Phone case with colourful illustrated print"></div>
    <div class="slide-case abs" style="left:520px;background:linear-gradient(#333,#111)" role="img" aria-label="Black smartphone"></div>
  </section>

  <aside class="side-box abs">
    <div class="side-head">Select Designs</div>
    <ul class="side-list">
      <li>Animals</li><li>Arts and Culture</li><li>Building and Environment</li><li>Business</li><li>Celebrations</li><li>Clothing</li><li>Decoration</li><li>Fantasy and Pictures</li><li>Food</li><li>Government</li><li>Grunge</li><li>Humor</li><li>Nature</li><li>People</li><li>Plants</li><li>Religion</li><li>School</li><li>Vehicles</li><li>Sports</li><li>Transportation</li>
    </ul>
  </aside>

  <aside class="subscribe abs">
    <h3>Subscribe</h3>
    <h4>Our Newsletters</h4>
    <p>Get new designs and special offers first.</p>
    <div class="field">Email address</div>
    <div class="go">Subscribe</div>
  </aside>

  <section class="grid abs">
    <div class="card"><div class="shot" style="background:linear-gradient(#8fd0f0,#f0a0c8)" role="img" aria-label="Blue and pink phone cases"></div><div class="name">Product Name</div><div class="price">$10.99</div><div class="cart">Add To Cart</div></div>
    <div class="card"><div class="shot" style="background:linear-gradient(#4a7ac0,#1d2f55)" role="img" aria-label="Blue smartphone"></div><div class="name">Product Name</div><div class="price">$3.99</div><div class="cart">Add To Cart</div></div>
    <div class="card"><div class="shot" style="background:linear-gradient(#e03030,#222)" role="img" aria-label="Red phone case"></div><div class="name">Product Name</div><div class="price">$8.99</div><div class="cart">Add To Cart</div></div>
    <div class="card"><div class="shot" style="background:linear-gradient(#444,#111)" role="img" aria-label="Black flip case"></div><div class="name">Product Name</div><div class="price">$13.45</div><div class="cart">Add To Cart</div></div>
    <div class="card"><div class="shot" style="background:linear-gradient(#f4f4f4,#f2b8cf)" role="img" aria-label="White and pink phone cases"></div><div class="name">Product Name</div><div class="price">$10.99</div><div class="cart">Add To Cart</div></div>
    <div class="card"><div class="shot" style="background:linear-gradient(#9ad04a,#3c3c3c)" role="img" aria-label="Green and black phone cases"></div><div class="name">Product Name</div><div class="price">$12.99</div><div class="cart">Add To Cart</div></div>
    <div class="card"><div class="shot" style="background:linear-gradient(#f6f6f6,#cfcfcf)" role="img" aria-label="White protective phone case"></div><div class="name">Product Name</div><div class="price">$9.99</div><div class="cart">Add To Cart</div></div>
    <div class="card"><div class="shot" style="background:linear-gradient(#3a3a3a,#0e0e0e)" role="img" aria-label="Black phone cases"></div><div class="name">Product Name</div><div class="price">$8.00</div><div class="cart">Add To Cart</div></div>
    <div class="card"><div class="shot" style="background:linear-gradient(#fafafa,#dcdcdc)" role="img" aria-label="White slim phone case"></div><div class="name">Product Name</div><div class="price">$7.49</div><div class="cart">Add To Cart</div></div>
  </section>

  <footer class="site-footer abs">
    <div class="f-col abs" style="left:30px"><h5>Information</h5><ul><li>Home</li><li>About Our Products</li><li>Buy or Selling</li><li>Delivery</li><li>Latest Product</li></ul></div>
    <div class="f-col abs" style="left:172px"><h5>Need Help</h5><ul><li>Privacy store</li><li>How to use online designer</li><li>Shopping Cart</li><li>Guarantee</li><li>Shipping information</li><li>Where is my order</li></ul></div>
    <div class="f-col abs" style="left:320px"><h5>About Us</h5><ul><li>About Us</li><li>Feedback</li><li>Privacy Policy</li><li>User Agreements</li><li>Submission information</li></ul></div>
    <div class="f-col abs" style="left:450px"><h5>Products</h5><ul><li>Home</li><li>About Our Products</li><li>Buy or Selling</li><li>Delivery</li><li>Latest Products</li></ul></div>
    <div class="f-col abs" style="left:580px"><h5>Get Connected</h5><div class="social"><b></b><b></b><b></b><b></b></div></div>
  </footer>
  <div class="footer-bar abs">
    <span class="copy abs">Copyright © 2013 Company name. All Rights Reserved</span>
    <span class="legal abs">Privacy Policy &nbsp;|&nbsp; Terms of Services</span>
  </div>

</div>
</body>
</html>
```